Android App Design Project

Hi my name is Karim, and I'm an android developer. I'm searching for a professional designer that can design my app.I have already launched the app and you can find it in the android market.

Main Requirements
- 15 sport icons
- 6 android pages
- Action bar
- Buttons and other icons

You need to do all requirements to submit a design. I need the design in both JPEG format and Photoshop PSD format. If you are interested then please download the PDF file ,it will help you a lot.
The name of the app is "MATCH VIEW Classic" you can find it in Nimbus Shelf.

NOTICE: You might read that the Payment is not guaranteed if I'm not happy with the design BUT if you make a good design and you win the contest, then you become my main designer that means if I want to change or add something to the design of the app in the future I return to you "the winner" directly to make the redesign and get paid for it.

Regards.
Talkwire: Rami Tohmeh "rami47"
E-mail: ramikarim@mailnest.example

Industry/Entity Type

Tv

Requirements
Must have
• - 15 sport icons
- 6 android pages
- Action bar
- Buttons and other icons

```html
<!DOCTYPE html>
<html lang="en">
<head>
<meta charset="utf-8">
<title>MATCH VIEW Classic – Score and Match List</title>
<link href="https://fonts.googleapis.com/css2?family=Arimo:wght@400;700&family=Oswald:wght@600&display=swap" rel="stylesheet">
<style>
  :root{
    --canvas:#1c1c20;
    --screen:#262626;
    --tile:#2d2d2d;
    --tile-edge:#1a1a1a;
    --bar-top:#3a3a3a;
    --bar-bottom:#232323;
    --status:#111111;
    --text:#f2f2f2;
    --muted:#c9c9c9;
    --accent:#f1a514;
    --live:#c8141a;
    --live-light:#ee3b3b;
    --badge:#e6a11a;
    --icon:#ededed;
  }
  *{box-sizing:border-box;margin:0;padding:0}
  html,body{width:1165px;height:1200px;overflow:hidden}
  body{background:var(--canvas);font-family:"Arimo",Arial,sans-serif;position:relative}

  .screen{position:absolute;width:328px;background:var(--screen);overflow:hidden;display:flex;flex-direction:column}
  .screen--grid{left:205px;top:217px;height:676px}
  .screen--list{left:650px;top:396px;height:494px}

  .status-bar{height:20px;background:var(--status);color:var(--text);font-size:12px;font-weight:700;display:flex;align-items:center;padding:0 8px;position:relative}
  .status-bar .signal{margin-right:3px}
  .status-bar .network{margin-left:8px}
  .status-bar .lock{position:absolute;left:157px;top:4px}
  .status-bar .battery{position:absolute;right:8px;top:6px}

  .action-bar{height:46px;background:linear-gradient(var(--bar-top),var(--bar-bottom));display:flex;align-items:center;padding:0 8px;border-bottom:1px solid #111}
  .action-bar .title{font-family:"Oswald",Arial,sans-serif;font-weight:600;font-size:20px;color:var(--muted);letter-spacing:.3px;margin-left:30px;flex:1}
  .action-bar svg{display:block;margin-left:10px}

  .tabs{height:33px;display:flex;background:linear-gradient(#333,#262626);border-bottom:1px solid #111}
  .tab{flex:1;color:var(--muted);font-size:18px;display:flex;align-items:center;justify-content:center}
  .tab + .tab{border-left:1px solid #1a1a1a}

  .sport-grid{display:grid;grid-template-columns:repeat(3,1fr);grid-template-rows:repeat(5,105px)}
  .sport{background:var(--tile);border-right:1px solid var(--tile-edge);border-bottom:1px solid var(--tile-edge);display:flex;flex-direction:column;align-items:center;justify-content:flex-start;padding-top:18px}
  .sport:nth-child(3n){border-right:none}
  .sport-icon{width:48px;height:48px;border-radius:50%;background:radial-gradient(circle at 40% 35%,#f4f4f4,#bdbdbd)}
  .sport-name{color:var(--accent);font-size:12px;font-weight:700;margin-top:auto;margin-bottom:10px;text-align:center;line-height:13px}

  .ad-banner{height:53px;margin-top:auto;display:flex;background:linear-gradient(90deg,#3b3733,#2a2724)}
  .ad-shot{width:98px;background:linear-gradient(#5a524a,#3a2f28)}
  .ad-brand{flex:1;display:flex;flex-direction:column;justify-content:center;padding-left:22px;color:#fff}
  .ad-brand .name{font-size:22px;font-weight:700;line-height:22px}
  .ad-brand .tag{font-size:11px;background:#fff;color:#222;align-self:flex-start;margin-left:50px;padding:0 4px}
  .ad-portrait{width:48px;background:linear-gradient(#8a7a6a,#3b3430)}

  .match-list{list-style:none}
  .match{height:58px;border-bottom:1px solid #151515;background:linear-gradient(#333,#262626);position:relative;padding:7px 0 0 20px;color:var(--text)}
  .match .time{font-size:14px;display:flex;align-items:center;gap:5px;color:#e6e6e6}
  .match .teams{font-size:17px;margin:4px 0 0 13px}
  .live{position:absolute;right:38px;top:12px;width:64px;height:24px;border-radius:12px;background:linear-gradient(var(--live-light),var(--live));color:#fff;font-weight:700;font-size:18px;display:flex;align-items:center;justify-content:center;border:1px solid #7a0a0a}
  .list-gap{height:28px;background:#2a2a2a}
  .screen--list .ad-banner{height:52px;margin-top:0}
</style>
</head>
<body>

<section class="screen screen--grid">
  <div class="status-bar">
    <svg class="signal" width="20" height="10"><rect x="0" y="8" width="2" height="2" fill="#fff"/><rect x="4" y="6" width="2" height="4" fill="#fff"/><rect x="8" y="4" width="2" height="6" fill="#fff"/><rect x="12" y="2" width="2" height="8" fill="#fff"/><rect x="16" y="0" width="2" height="10" fill="#fff"/></svg>
    <span>NOVA</span><span class="network">3G</span>
    <svg class="lock" width="10" height="12"><path d="M2 6V4a3 3 0 0 1 6 0v2" stroke="#fff" stroke-width="1.5" fill="none"/><rect x="1" y="6" width="8" height="6" fill="#fff"/></svg>
    <svg class="battery" width="22" height="9"><rect x=".5" y=".5" width="19" height="8" stroke="#fff" fill="none"/><rect x="2" y="2" width="16" height="5" fill="#fff"/><rect x="20" y="3" width="2" height="3" fill="#fff"/></svg>
  </div>
  <header class="action-bar">
    <svg width="38" height="28"><rect x="1" y="1" width="36" height="26" rx="4" fill="#555" stroke="#777"/><rect x="5" y="5" width="28" height="18" rx="2" fill="#2a2a2a"/></svg>
    <span class="title">SPORT TITLE</span>
    <svg width="24" height="22"><path d="M2 20c0-9 6-13 13-13V2l8 8-8 8v-5c-6 0-10 2-13 7z" fill="#444" stroke="#666"/></svg>
    <svg width="30" height="28"><path d="M4 22h20l-3-4v-6a6 6 0 0 0-12 0v6z" fill="#111"/><circle cx="14" cy="25" r="2.5" fill="#111"/><circle cx="22" cy="8" r="7" fill="var(--badge)"/><text x="22" y="12" font-size="10" text-anchor="middle" fill="#333" font-family="Arimo, sans-serif">5</text></svg>
    <svg width="26" height="26"><circle cx="13" cy="13" r="12" fill="#111" stroke="#444"/><text x="13" y="19" font-size="16" font-style="italic" font-weight="700" text-anchor="middle" fill="#aaa" font-family="Georgia, serif">i</text></svg>
  </header>
  <nav class="tabs"><span class="tab">SCORE</span><span class="tab">NEWS</span></nav>
  <div class="sport-grid">
    <div class="sport"><span class="sport-icon" role="img" aria-label="Football icon"></span><span class="sport-name">FOOTBALL</span></div>
    <div class="sport"><span class="sport-icon" role="img" aria-label="Volleyball icon"></span><span class="sport-name">VOLLEYBALL</span></div>
    <div class="sport"><span class="sport-icon" role="img" aria-label="Rugby ball icon"></span><span class="sport-name">RUGBY</span></div>
    <div class="sport"><span class="sport-icon" role="img" aria-label="Skier pictogram"></span><span class="sport-name">WINTERSPORT</span></div>
    <div class="sport"><span class="sport-icon" role="img" aria-label="Boxing gloves icon"></span><span class="sport-name">BOXING</span></div>
    <div class="sport"><span class="sport-icon" role="img" aria-label="Cricket bat and ball icon"></span><span class="sport-name">CRICKET</span></div>
    <div class="sport"><span class="sport-icon" role="img" aria-label="Basketball icon"></span><span class="sport-name">BASKETBALL</span></div>
    <div class="sport"><span class="sport-icon" role="img" aria-label="Dart icon"></span><span class="sport-name">DARTS</span></div>
    <div class="sport"><span class="sport-icon" role="img" aria-label="Wrestlers pictogram"></span><span class="sport-name">WRESTLING</span></div>
    <div class="sport"><span class="sport-icon" role="img" aria-label="Tennis player pictogram"></span><span class="sport-name">TENNIS</span></div>
    <div class="sport"><span class="sport-icon" role="img" aria-label="American football icon"></span><span class="sport-name">AMERICAN<br>FOOTBALL</span></div>
    <div class="sport"><span class="sport-icon" role="img" aria-label="Futsal player pictogram"></span><span class="sport-name">FUTSAL</span></div>
    <div class="sport"><span class="sport-icon" role="img" aria-label="Shuttlecock icon"></span><span class="sport-name">BADMINTON</span></div>
    <div class="sport"><span class="sport-icon" role="img" aria-label="Handball player pictogram"></span><span class="sport-name">HANDBALL</span></div>
    <div class="sport"><span class="sport-icon" role="img" aria-label="Ice hockey player pictogram"></span><span class="sport-name">ICE HOCKEY</span></div>
  </div>
  <aside class="ad-banner">
    <div class="ad-shot" role="img" aria-label="Recipe app screenshot with plated dish"></div>
    <div class="ad-brand"><span class="name">Cook Nook</span><span class="tag">quick plates</span></div>
    <div class="ad-portrait" role="img" aria-label="Chef portrait"></div>
  </aside>
</section>

<section class="screen screen--list">
  <div class="status-bar">
    <svg class="signal" width="20" height="10"><rect x="0" y="8" width="2" height="2" fill="#fff"/><rect x="4" y="6" width="2" height="4" fill="#fff"/><rect x="8" y="4" width="2" height="6" fill="#fff"/><rect x="12" y="2" width="2" height="8" fill="#fff"/><rect x="16" y="0" width="2" height="10" fill="#fff"/></svg>
    <span>NOVA</span><span class="network">3G</span>
    <svg class="lock" width="10" height="12"><path d="M2 6V4a3 3 0 0 1 6 0v2" stroke="#fff" stroke-width="1.5" fill="none"/><rect x="1" y="6" width="8" height="6" fill="#fff"/></svg>
    <svg class="battery" width="22" height="9"><rect x=".5" y=".5" width="19" height="8" stroke="#fff" fill="none"/><rect x="2" y="2" width="16" height="5" fill="#fff"/><rect x="20" y="3" width="2" height="3" fill="#fff"/></svg>
  </div>
  <header class="action-bar">
    <svg width="38" height="28"><rect x="1" y="1" width="36" height="26" rx="4" fill="#555" stroke="#777"/><rect x="5" y="5" width="28" height="18" rx="2" fill="#2a2a2a"/></svg>
    <span class="title">SPORT TITLE</span>
    <svg width="24" height="22"><path d="M2 20c0-9 6-13 13-13V2l8 8-8 8v-5c-6 0-10 2-13 7z" fill="#444" stroke="#666"/></svg>
    <svg width="30" height="28"><path d="M4 22h20l-3-4v-6a6 6 0 0 0-12 0v6z" fill="#111"/><circle cx="14" cy="25" r="2.5" fill="#111"/><circle cx="22" cy="8" r="7" fill="var(--badge)"/><text x="22" y="12" font-size="10" text-anchor="middle" fill="#333" font-family="Arimo, sans-serif">5</text></svg>
    <svg width="26" height="26"><circle cx="13" cy="13" r="12" fill="#111" stroke="#444"/><text x="13" y="19" font-size="16" font-style="italic" font-weight="700" text-anchor="middle" fill="#aaa" font-family="Georgia, serif">i</text></svg>
  </header>
  <ul class="match-list">
    <li class="match"><span class="time"><svg width="9" height="9"><circle cx="4.5" cy="4.5" r="3.8" stroke="#ddd" fill="none"/><path d="M4.5 2v2.5h2" stroke="#ddd" fill="none"/></svg>Time - 16:00</span><p class="teams">Iraq vs Kuwait</p><span class="live">LIVE</span></li>
    <li class="match"><span class="time"><svg width="9" height="9"><circle cx="4.5" cy="4.5" r="3.8" stroke="#ddd" fill="none"/><path d="M4.5 2v2.5h2" stroke="#ddd" fill="none"/></svg>Time - 16:00</span><p class="teams">India vs England</p></li>
    <li class="match"><span class="time"><svg width="9" height="9"><circle cx="4.5" cy="4.5" r="3.8" stroke="#ddd" fill="none"/><path d="M4.5 2v2.5h2" stroke="#ddd" fill="none"/></svg>Time - 16:00</span><p class="teams">yemen&nbsp; vs Saudi Arbia</p></li>
    <li class="match"><span class="time"><svg width="9" height="9"><circle cx="4.5" cy="4.5" r="3.8" stroke="#ddd" fill="none"/><path d="M4.5 2v2.5h2" stroke="#ddd" fill="none"/></svg>Time - 16:00</span><p class="teams">Iraq vs Kuwait</p><span class="live">LIVE</span></li>
    <li class="match"><span class="time"><svg width="9" height="9"><circle cx="4.5" cy="4.5" r="3.8" stroke="#ddd" fill="none"/><path d="M4.5 2v2.5h2" stroke="#ddd" fill="none"/></svg>Time - 16:00</span><p class="teams">Iraq vs Kuwait</p></li>
    <li class="match"><span class="time"><svg width="9" height="9"><circle cx="4.5" cy="4.5" r="3.8" stroke="#ddd" fill="none"/><path d="M4.5 2v2.5h2" stroke="#ddd" fill="none"/></svg>Time - 16:00</span><p class="teams">Bangladesh vs Iran</p></li>
  </ul>
  <div class="list-gap"></div>
  <aside class="ad-banner">
    <div class="ad-shot" role="img" aria-label="Recipe app screenshot with plated dish"></div>
    <div class="ad-brand"><span class="name">Cook Nook</span><span class="tag">quick plates</span></div>
    <div class="ad-portrait" role="img" aria-label="Chef portrait"></div>
  </aside>
</section>

</body>
</html>
```